Managed Service Provider need new business cards

We are a small Maanged Service Provider of IT Services and need a new fresh design for our business cards. We want something impossible, fun and professional :)
Our services has a large range, but we are always fun and make sure our customers both get their issue sorted and also feel like they are "catching up with an old friend".
All our cards in the past has always been all black, with red and we need something fresher.
The back of card, we would like just a small list of what we do i think, but if someone has a better idea, please do something cool with the back of the card:
Managed IT Services
Productivity Solutions
Data Backup and Recovery
IT System Maintenance
Managed IT Security
More details can be found on our website tqnetworks.com.au
Industry/Entity Type
It Company
Contact Information for Business Card
Name: Dwayne Falstrup
Title: Director
Phone: 03 6193 4827
Mobile: 0412 587 239
Email: dwayne@tqnetworks.com.au
Web: www.tqnetworks.com.au

```html
<!DOCTYPE html>
<html lang="en">
<head>
<meta charset="utf-8">
<title>TQ Networks – Business Card</title>
<link rel="stylesheet" href="https://fonts.googleapis.com/css2?family=Josefin+Sans:wght@300;400;600;700&display=swap">
<style>
  :root {
    --page-bg: #e4e7eb;
    --card-top: #f5f5f5;
    --card-edge: #e6e7e9;
    --band-dark: #1c1c1d;
    --band-mid: #2a2a2b;
    --brand-red: #d8262b;
    --accent-red: #b51a1f;
    --text-dark: #232323;
    --text-light: #e6e6e6;
    --text-soft: #cfcfcf;
  }
  html, body {
    margin: 0;
    width: 1200px;
    height: 894px;
    overflow: hidden;
    background: var(--page-bg);
    font-family: "Josefin Sans", sans-serif;
  }
  .card {
    position: absolute;
    left: 80px;
    top: 152px;
    width: 1040px;
    height: 590px;
    border-radius: 44px;
    background: var(--card-edge);
    overflow: hidden;
    box-shadow: 0 14px 40px rgba(0,0,0,0.18);
  }
  .card-top {
    position: absolute;
    left: 0; top: 0;
    width: 100%;
    height: 287px;
    background: var(--card-top);
  }
  .brand {
    position: absolute;
    left: 44px;
    top: 92px;
    display: flex;
    align-items: center;
    gap: 18px;
  }
  .brand-dot {
    width: 34px;
    height: 34px;
    border-radius: 50%;
    background: var(--brand-red);
  }
  .brand-name {
    font-weight: 700;
    font-size: 62px;
    line-height: 1;
    color: var(--brand-red);
    letter-spacing: 1px;
    padding-top: 8px;
  }
  .services {
    position: absolute;
    left: 636px;
    top: 52px;
    margin: 0;
    padding: 0;
    list-style: none;
  }
  .services li {
    position: relative;
    padding-left: 27px;
    font-size: 27px;
    line-height: 41px;
    color: var(--text-dark);
    font-weight: 400;
    letter-spacing: 0.5px;
  }
  .services li::before {
    content: "";
    position: absolute;
    left: 0;
    top: 13px;
    width: 11px;
    height: 11px;
    border-radius: 50%;
    background: var(--brand-red);
  }
  .contact-band {
    position: absolute;
    left: 0;
    top: 287px;
    width: 100%;
    height: 269px;
    background: linear-gradient(90deg, var(--band-dark) 0%, var(--band-mid) 35%, var(--band-dark) 58%, var(--accent-red) 85%, var(--accent-red) 100%);
  }
  .person-name {
    position: absolute;
    left: 42px;
    top: 18px;
    margin: 0;
    font-size: 37px;
    font-weight: 600;
    color: var(--brand-red);
    letter-spacing: 0.5px;
  }
  .person-title {
    position: absolute;
    left: 42px;
    top: 62px;
    margin: 0;
    font-size: 26px;
    font-weight: 300;
    color: var(--text-soft);
    letter-spacing: 0.5px;
  }
  .contacts {
    position: absolute;
    left: 42px;
    top: 117px;
    margin: 0;
    padding: 0;
    list-style: none;
  }
  .contacts li {
    display: flex;
    align-items: center;
    gap: 14px;
    height: 35px;
    font-size: 27px;
    font-weight: 300;
    color: var(--text-light);
    letter-spacing: 0.3px;
  }
  .contacts .icon {
    width: 24px;
    height: 24px;
    flex: none;
  }
  .contacts .no-icon { width: 24px; flex: none; }
  .card-foot {
    position: absolute;
    left: 0;
    bottom: 0;
    width: 100%;
    height: 34px;
    background: var(--card-edge);
  }
</style>
</head>
<body>
  <div class="card">
    <section class="card-top">
      <div class="brand">
        <span class="brand-dot"></span>
        <span class="brand-name">TQ NETWORKS</span>
      </div>
      <ul class="services">
        <li>Managed IT Services</li>
        <li>Productivity Solutions</li>
        <li>Data Backup and Recovery</li>
        <li>IT System Maintenance</li>
        <li>Managed IT Security</li>
      </ul>
    </section>

    <section class="contact-band">
      <h1 class="person-name">Dwayne Falstrup</h1>
      <p class="person-title">Director</p>
      <ul class="contacts">
        <li>
          <svg class="icon" viewBox="0 0 24 24" aria-hidden="true">
            <circle cx="12" cy="12" r="12" fill="#d8262b"/>
            <path d="M6 10c0-2 3-3.5 6-3.5s6 1.5 6 3.5l-2.2.6-.6-1.6h-6.4l-.6 1.6zM7.5 12h9l1 5h-11z" fill="#1c1c1d"/>
          </svg>
          <span>03 6193 4827</span>
        </li>
        <li>
          <svg class="icon" viewBox="0 0 24 24" aria-hidden="true">
            <circle cx="12" cy="12" r="12" fill="#d8262b"/>
            <rect x="8" y="5" width="8" height="14" rx="1.5" fill="#1c1c1d"/>
            <rect x="9.3" y="6.8" width="5.4" height="9" fill="#d8262b"/>
          </svg>
          <span>0412 587 239</span>
        </li>
        <li>
          <svg class="icon" viewBox="0 0 24 24" aria-hidden="true">
            <circle cx="12" cy="12" r="12" fill="#d8262b"/>
            <rect x="5.5" y="7.5" width="13" height="9" fill="#1c1c1d"/>
            <path d="M5.5 7.5l6.5 5 6.5-5" fill="none" stroke="#d8262b" stroke-width="1.3"/>
          </svg>
          <span>dwayne@tqnetworks.com.au</span>
        </li>
        <li>
          <span class="no-icon"></span>
          <span>www.tqnetworks.com.au</span>
        </li>
      </ul>
    </section>

    <div class="card-foot"></div>
  </div>
</body>
</html>
```